Life Coach for Lawyers Business Card Design

Elegant, original, business card design for life coaching service for associate attorneys who work in big law and struggle with stress, overwhelm, and time management. Double sided design.

Target Market(s)

Women associate attorneys who work in big law and struggle with stress, overwhelm, and time management.

Industry/Entity Type

Life Coaching

Contact Information for Business Card

Marissa Pendrell
Life Coach
518.677.3941
calmbriefcounsel.net
marissa@calmbriefcounsel.net
@calmbriefcounsel (Instagram)

Font styles to use
Other font styles liked:
• Silver South font duo. See uploaded files.

Requirements
Must have
• Icons for phone, website, email, and Instagram instead of words. Specific colors used in my logo (171B2B, 421121, FFFFFF)
Nice to have
• Foil. Embossed. Feminine design.
Should not have
• Any colors other than those used in logo. See uploaded files.

```html
<!DOCTYPE html>
<html lang="en">
<head>
<meta charset="utf-8">
<title>Calm Brief Counsel — Business Card</title>
<link href="https://fonts.googleapis.com/css2?family=Montserrat:wght@500;700&family=Roboto:wght@400&display=swap" rel="stylesheet">
<style>
  :root {
    --stage: #1b1b1d;
    --card: #421121;
    --card-light: #4f1f2c;
    --ink: #ffffff;
    --navy: #171b2b;
  }
  * { margin: 0; padding: 0; box-sizing: border-box; }
  html, body {
    width: 1200px; height: 900px; overflow: hidden;
    background: var(--stage);
  }
  .canvas {
    position: relative; width: 1200px; height: 900px;
    display: flex; flex-direction: column; align-items: center; justify-content: center; gap: 34px;
  }
  .card {
    width: 700px; height: 400px;
    background: linear-gradient(135deg, var(--card) 0%, var(--card) 55%, var(--card-light) 100%);
    color: var(--ink);
    position: relative;
    box-shadow: 0 10px 30px rgba(0,0,0,.45);
  }
  /* Front */
  .card-front { display: flex; align-items: center; justify-content: center; }
  .brand-mark { display: flex; align-items: center; gap: 16px; }
  .brand-dot {
    width: 22px; height: 22px; border-radius: 50%;
    border: 1.5px solid var(--ink);
  }
  .brand-name {
    font-family: "Montserrat", sans-serif; font-weight: 500;
    font-size: 26px; letter-spacing: 4px; text-transform: uppercase;
  }
  /* Back */
  .card-back { display: flex; align-items: center; padding: 0 30px 0 50px; }
  .back-brand {
    width: 250px; flex: none;
    font-family: "Montserrat", sans-serif; font-weight: 500;
    font-size: 32px; line-height: 1.15; letter-spacing: 3px; text-transform: uppercase;
  }
  .divider { width: 1.5px; height: 200px; background: var(--ink); margin: 0 30px 0 14px; flex: none; }
  .contact { font-family: "Roboto", sans-serif; font-size: 17px; line-height: 1.5; white-space: nowrap; }
  .contact-name {
    font-family: "Montserrat", sans-serif; font-weight: 700;
    font-size: 25px; text-transform: uppercase; letter-spacing: .5px; line-height: 1.1;
  }
  .contact-role { font-size: 17px; margin-bottom: 18px; }
  .contact-row { display: flex; align-items: center; gap: 10px; }
  .contact-row svg { width: 13px; height: 13px; flex: none; }
</style>
</head>
<body>
<main class="canvas">
  <section class="card card-front" aria-label="Card front">
    <div class="brand-mark">
      <span class="brand-dot"></span>
      <span class="brand-name">Calm Brief Counsel</span>
    </div>
  </section>

  <section class="card card-back" aria-label="Card back">
    <div class="back-brand">Calm Brief Counsel</div>
    <div class="divider"></div>
    <div class="contact">
      <div class="contact-name">Marissa Pendrell</div>
      <div class="contact-role">Life Coach</div>
      <div class="contact-row">
        <svg viewBox="0 0 24 24" fill="#fff" aria-hidden="true"><path d="M6.6 10.8a15 15 0 0 0 6.6 6.6l2.2-2.2c.3-.3.7-.4 1-.2 1.1.4 2.3.6 3.6.6.6 0 1 .4 1 1V20c0 .6-.4 1-1 1A17 17 0 0 1 3 4c0-.6.4-1 1-1h3.5c.6 0 1 .4 1 1 0 1.3.2 2.5.6 3.6.1.3 0 .7-.2 1z"/></svg>
        <span>518-677-3941</span>
      </div>
      <div class="contact-row">
        <svg viewBox="0 0 24 24" fill="none" stroke="#fff" stroke-width="2" aria-hidden="true"><rect x="3" y="5" width="18" height="14" rx="1"/><path d="M3 6l9 7 9-7"/></svg>
        <span>marissa@calmbriefcounsel.net</span>
      </div>
      <div class="contact-row">
        <svg viewBox="0 0 24 24" fill="none" stroke="#fff" stroke-width="2" aria-hidden="true"><circle cx="12" cy="12" r="9"/><path d="M3 12h18M12 3c3 3 3 15 0 18M12 3c-3 3-3 15 0 18"/></svg>
        <span>www.calmbriefcounsel.net</span>
      </div>
      <div class="contact-row">
        <svg viewBox="0 0 24 24" fill="none" stroke="#fff" stroke-width="2" aria-hidden="true"><circle cx="12" cy="12" r="9"/></svg>
        <span>@calmbriefcounsel</span>
      </div>
    </div>
  </section>
</main>
</body>
</html>
```